Update existing icons for an admin interface to look more professional high end

Please see attached 4 files.
One from a competitor system which looks more high end and our icon files and how they look in the interface.
We need to suit to high end network administrators and need a more professional high end look. They need be in the same blueish color theme.

```html
<!DOCTYPE html>
<html lang="en">
<head>
<meta charset="utf-8">
<title>Admin Navigation Menus</title>
<link href="https://fonts.googleapis.com/css2?family=Source+Sans+3:wght@600&display=swap" rel="stylesheet">
<style>
  :root {
    --page-bg: #ffffff;
    --frame-bg: #0c1213;
    --menu-bg: #233140;
    --divider: #131c25;
    --header-top: #4a5b6a;
    --header-bottom: #2c3c4a;
    --header-edge: #8598a6;
    --icon-blue: #3d7fea;
    --icon-light: #8fb6f5;
    --alert-red: #e0202a;
    --label: #eef3f8;
  }
  html, body { margin: 0; padding: 0; width: 1200px; height: 1200px; overflow: hidden; background: var(--page-bg); }
  .canvas { position: relative; width: 1200px; height: 1200px; }
  .frame { position: absolute; left: 516px; top: 29px; width: 158px; height: 1133px; background: var(--frame-bg); }
  .menu { position: absolute; left: 523px; width: 134px; background: var(--menu-bg); }
  .menu-header {
    position: absolute; left: 523px; width: 134px; height: 22px; box-sizing: border-box;
    border: 1px solid var(--header-edge); border-bottom: none; border-radius: 3px 3px 0 0;
    background: linear-gradient(var(--header-top), var(--header-bottom));
    display: flex; align-items: center; justify-content: center; gap: 5px;
  }
  .divider { position: absolute; left: 523px; width: 134px; height: 1px; background: var(--divider); }
  .item { position: absolute; left: 529px; height: 20px; display: flex; align-items: center; gap: 4px; white-space: nowrap; }
  .label, .menu-header span {
    font-family: "Source Sans 3", sans-serif; font-weight: 600; font-size: 11.8px;
    letter-spacing: -0.35px; color: var(--label);
  }
  .icon { width: 16px; height: 16px; flex: none; }
  .defs { position: absolute; width: 0; height: 0; }
</style>
</head>
<body>
<div class="canvas">
  <svg class="defs" aria-hidden="true">
    <defs>
      <symbol id="i-monitor" viewBox="0 0 16 16"><rect x="1" y="2" width="14" height="9" fill="#3d7fea"/><rect x="3" y="4" width="10" height="5" fill="#8fb6f5"/><rect x="6" y="11" width="4" height="2" fill="#3d7fea"/><rect x="4" y="13" width="8" height="1.5" fill="#3d7fea"/></symbol>
      <symbol id="i-chart" viewBox="0 0 16 16"><path d="M1 1v14h14" stroke="#3d7fea" stroke-width="2" fill="none"/><path d="M3 12l3-5 3 3 5-7" stroke="#3d7fea" stroke-width="2" fill="none"/></symbol>
      <symbol id="i-spam" viewBox="0 0 16 16"><rect x="0" y="4" width="13" height="8" fill="#3d7fea"/><circle cx="13" cy="12" r="3" fill="none" stroke="#e0202a" stroke-width="1.5"/><path d="M11 14l4-4" stroke="#e0202a" stroke-width="1.5"/></symbol>
      <symbol id="i-archive" viewBox="0 0 16 16"><rect x="1" y="6" width="14" height="9" fill="#3d7fea"/><rect x="4" y="1" width="8" height="7" fill="#8fb6f5"/><path d="M1 6l7 5 7-5" stroke="#233140" fill="none"/></symbol>
      <symbol id="i-shield" viewBox="0 0 16 16"><path d="M8 1l6 2v5c0 4-3 6-6 7-3-1-6-3-6-7V3z" fill="#3d7fea"/><path d="M8 1v14" stroke="#8fb6f5"/></symbol>
      <symbol id="i-mail" viewBox="0 0 16 16"><rect x="0" y="3" width="16" height="11" fill="#3d7fea"/></symbol>
      <symbol id="i-firewall" viewBox="0 0 16 16"><rect x="0" y="6" width="13" height="9" fill="#3d7fea"/><path d="M13 1c2 3 2 5 0 7-1-1-1-3 0-7z" fill="#e0202a"/></symbol>
      <symbol id="i-vpn" viewBox="0 0 16 16"><rect x="1" y="1" width="14" height="10" fill="none" stroke="#3d7fea" stroke-width="1.6"/><path d="M4 6h8M4 6l2-2M12 6l-2 2" stroke="#8fb6f5" stroke-width="1.3" fill="none"/><rect x="3" y="13" width="10" height="2" fill="#3d7fea"/></symbol>
      <symbol id="i-globe" viewBox="0 0 16 16"><circle cx="8" cy="8" r="7.5" fill="#3d7fea"/><path d="M1 8h14M4 5v6M8 3v10M12 5v6" stroke="#8fb6f5" stroke-width="1"/></symbol>
      <symbol id="i-traffic" viewBox="0 0 16 16"><rect x="0.5" y="0.5" width="15" height="15" rx="5" fill="#3d7fea"/><path d="M3 9l3-3 3 3 4-4" stroke="#8fb6f5" stroke-width="1.2" fill="none"/></symbol>
      <symbol id="i-ips" viewBox="0 0 16 16"><circle cx="3.5" cy="8" r="2.5" fill="none" stroke="#3d7fea" stroke-width="1.5"/><circle cx="9.5" cy="8" r="2.5" fill="none" stroke="#3d7fea" stroke-width="1.5"/><path d="M13 6l2 2-2 2" stroke="#3d7fea" stroke-width="1.5" fill="none"/></symbol>
      <symbol id="i-wifi" viewBox="0 0 16 16"><path d="M1 6a10 10 0 0 1 14 0L8 13z" fill="#3d7fea"/><path d="M4 8.5a6 6 0 0 1 8 0" stroke="#8fb6f5" fill="none"/><rect x="7" y="12" width="2" height="3" fill="#3d7fea"/></symbol>
      <symbol id="i-funnel" viewBox="0 0 16 16"><path d="M0 1h16l-6 7v7l-4-2V8z" fill="#3d7fea"/></symbol>
      <symbol id="i-scanner" viewBox="0 0 16 16"><circle cx="6.5" cy="6.5" r="5" fill="none" stroke="#3d7fea" stroke-width="2"/><circle cx="6.5" cy="6.5" r="2.5" fill="#8fb6f5"/><path d="M10.3 10.3l4.5 4.5" stroke="#3d7fea" stroke-width="2.6" stroke-linecap="round"/></symbol>
      <symbol id="i-gauge" viewBox="0 0 16 16"><path d="M1 13a7 7 0 1 1 14 0z" fill="none" stroke="#3d7fea" stroke-width="2"/><path d="M8 12l4-5" stroke="#3d7fea" stroke-width="2"/></symbol>
      <symbol id="i-user" viewBox="0 0 16 16"><circle cx="8" cy="5" r="4" fill="#3d7fea"/><path d="M0 16c0-5 4-7 8-7s8 2 8 7z" fill="#3d7fea"/></symbol>
      <symbol id="i-gear" viewBox="0 0 16 16"><circle cx="8" cy="8" r="6" fill="none" stroke="#3d7fea" stroke-width="3.5" stroke-dasharray="2.4 1.3"/><circle cx="8" cy="8" r="4.5" fill="#3d7fea"/><circle cx="8" cy="8" r="2" fill="#233140"/></symbol>
      <symbol id="i-network" viewBox="0 0 16 16"><rect x="0" y="1" width="7" height="5" fill="#3d7fea"/><rect x="9" y="1" width="7" height="5" fill="#3d7fea"/><path d="M3.5 6v3h9V6M8 9v4" stroke="#3d7fea" stroke-width="1.6" fill="none"/><rect x="5.5" y="12" width="5" height="4" fill="#3d7fea"/></symbol>
      <symbol id="i-info" viewBox="0 0 16 16"><circle cx="8" cy="8" r="8" fill="#3d7fea"/><rect x="7.3" y="4" width="1.4" height="6" fill="#8fb6f5"/></symbol>
      <symbol id="i-update" viewBox="0 0 16 16"><path d="M14 8a6 6 0 1 1-2-4.5" stroke="#3d7fea" stroke-width="2.4" fill="none"/><path d="M10 1l4 2-3 3z" fill="#3d7fea"/></symbol>
      <symbol id="i-support" viewBox="0 0 16 16"><circle cx="8" cy="8" r="6" fill="none" stroke="#3d7fea" stroke-width="3.5"/><path d="M3.5 3.5l3 3M12.5 3.5l-3 3M3.5 12.5l3-3M12.5 12.5l-3-3" stroke="#8fb6f5" stroke-width="1.4"/></symbol>
      <symbol id="i-clock" viewBox="0 0 16 16"><circle cx="8" cy="8" r="8" fill="#3d7fea"/><path d="M8 3v5H4" stroke="#8fb6f5" stroke-width="1.4" fill="none"/></symbol>
      <symbol id="i-ticket" viewBox="0 0 16 16"><path d="M10 1l5 5-9 9-5-5z" fill="#3d7fea"/><path d="M7 5l4 4" stroke="#8fb6f5" stroke-dasharray="1 1"/></symbol>
    </defs>
  </svg>

  <div class="frame"></div>

  <!-- Appliance menu -->
  <div class="menu-header" style="top:38px"><svg class="icon"><use href="#i-monitor"/></svg><span>Home</span></div>
  <div class="menu" style="top:62px;height:678px"></div>
  <div class="divider" style="top:130px"></div>
  <div class="divider" style="top:197px"></div>
  <div class="divider" style="top:265px"></div>
  <div class="divider" style="top:503px"></div>
  <div class="divider" style="top:570px"></div>
  <div class="divider" style="top:638px"></div>
  <div class="divider" style="top:706px"></div>

  <div class="item" style="top:68px"><svg class="icon"><use href="#i-chart"/></svg><span class="label">Statistics &amp; Logos</span></div>
  <div class="item" style="top:102px"><svg class="icon"><use href="#i-spam"/></svg><span class="label">Anti Spam</span></div>
  <div class="item" style="top:138px"><svg class="icon"><use href="#i-archive"/></svg><span class="label">Mail Archiver</span></div>
  <div class="item" style="top:171px"><svg class="icon"><use href="#i-shield"/></svg><span class="label">Anti Virus</span></div>
  <div class="item" style="top:206px"><svg class="icon"><use href="#i-mail"/></svg><span class="label">E-Mail</span></div>
  <div class="item" style="top:240px"><svg class="icon"><use href="#i-firewall"/></svg><span class="label">Firewall</span></div>
  <div class="item" style="top:273px"><svg class="icon"><use href="#i-vpn"/></svg><span class="label">VPN</span></div>
  <div class="item" style="top:307px"><svg class="icon"><use href="#i-globe"/></svg><span class="label">Web Filter</span></div>
  <div class="item" style="top:339px"><svg class="icon"><use href="#i-traffic"/></svg><span class="label">Traffic Shaper</span></div>
  <div class="item" style="top:374px"><svg class="icon"><use href="#i-ips"/></svg><span class="label">IPS - Malware</span></div>
  <div class="item" style="top:409px"><svg class="icon"><use href="#i-wifi"/></svg><span class="label">WiFi Defender</span></div>
  <div class="item" style="top:442px"><svg class="icon"><use href="#i-funnel"/></svg><span class="label">Content Filter</span></div>
  <div class="item" style="top:475px"><svg class="icon"><use href="#i-scanner"/></svg><span class="label">Vulnerability Scanner</span></div>
  <div class="item" style="top:510px"><svg class="icon"><use href="#i-gauge"/></svg><span class="label">Alert Center</span></div>
  <div class="item" style="top:543px"><svg class="icon"><use href="#i-user"/></svg><span class="label">Protector User</span></div>
  <div class="item" style="top:577px"><svg class="icon"><use href="#i-gear"/></svg><span class="label">System</span></div>
  <div class="item" style="top:610px"><svg class="icon"><use href="#i-network"/></svg><span class="label">Network Setup</span></div>
  <div class="item" style="top:645px"><svg class="icon"><use href="#i-info"/></svg><span class="label">High Availability</span></div>
  <div class="item" style="top:678px"><svg class="icon"><use href="#i-update"/></svg><span class="label">Update</span></div>
  <div class="item" style="top:712px"><svg class="icon"><use href="#i-support"/></svg><span class="label">Suport</span></div>

  <!-- Scanner menu -->
  <div class="menu-header" style="top:755px"><svg class="icon"><use href="#i-monitor"/></svg><span>Home</span></div>
  <div class="menu" style="top:778px;height:373px"></div>
  <div class="divider" style="top:1084px"></div>

  <div class="item" style="top:784px"><svg class="icon"><use href="#i-scanner"/></svg><span class="label">Vulnerability Scanner</span></div>
  <div class="item" style="top:819px"><svg class="icon"><use href="#i-clock"/></svg><span class="label">Schedule</span></div>
  <div class="item" style="top:853px"><svg class="icon"><use href="#i-chart"/></svg><span class="label">Statistics</span></div>
  <div class="item" style="top:886px"><svg class="icon"><use href="#i-ticket"/></svg><span class="label">Tickets</span></div>
  <div class="item" style="top:921px"><svg class="icon"><use href="#i-wifi"/></svg><span class="label">WiFi Pen Test</span></div>
  <div class="item" style="top:956px"><svg class="icon"><use href="#i-user"/></svg><span class="label">Cloud Users</span></div>
  <div class="item" style="top:988px"><svg class="icon"><use href="#i-vpn"/></svg><span class="label">Scan Distribution</span></div>
  <div class="item" style="top:1022px"><svg class="icon"><use href="#i-gear"/></svg><span class="label">System</span></div>
  <div class="item" style="top:1056px"><svg class="icon"><use href="#i-network"/></svg><span class="label">Network Setup</span></div>
  <div class="item" style="top:1088px"><svg class="icon"><use href="#i-update"/></svg><span class="label">Update</span></div>
  <div class="item" style="top:1123px"><svg class="icon"><use href="#i-support"/></svg><span class="label">Support</span></div>
</div>
</body>
</html>
```